New Design for our Credit Cards tank.

Our company has petrol stations in Spain and the rest of Europe. We are specialized on the international transport companies. For This We Have our own "credit cards tank" With These cards you can refill in different countries (all over Europe) fast, save and cheap. We would like to redesign our credit cards tank. We are looking for something more modern, elegant and clean. We have three card types: - Spanish Card (Spain Card): This card is for customers who make refills at our service stations in Spain. This card is for Diesel product and used by transport companies. The printer prints the data That on This card can print in white. The fields we are print on the card, card number, holder, registration number and expiration date. - Europe Card (Europe Card): This card is for customers who refills at our service stations in Europe. The printer prints the data That on This card can not print in white. The fields we are print on the card, card number, holder, registration number and expiration date. - Red Card (Gasoleo Bonificado): This card is for a Customer WHO refills Red Diesel for a refrigerator units in our service stations in Spain. The printer prints the data That on This card can print in white. The fields we are print on the card, card number, holder, registration number and expiration date. Very important for us is That on the back side, you respect the text shown on the cards and the magnetic stripe zone. Of course Also the name of the company BRENVICOR must be seen there. Also would be great if our colors (its blue colors) will be respected. If You have any questions or Suggest we are pleased to get your comments or contacts. Thanks in advance Brenvicor

Target Market(s)

Our customers

Industry/Entity Type

Credit Card

Font styles to use
Sans Serif

Colors
3176b5
0255a3
85acd3
cedeed
85cae6
33a6d7
0692cd
f59195
f04a50

Requirements
Must have
• The only thing we Have to keep the fields on front and back text. The credit card 85mm x 54mm are meassures.

```html
<!DOCTYPE html>
<html lang="es">
<head>
<meta charset="utf-8">
<title>Brenvicor – Tarjetas de carburante</title>
<link rel="stylesheet" href="https://fonts.googleapis.com/css2?family=Nunito:ital,wght@0,300;0,400;1,400;1,600&family=Poppins:wght@300&display=swap">
<style>
  :root{
    --page:#ffffff;
    --ink:#1c1c1c;
    --stripe:#262626;
    --espana-1:#0a2f8f;
    --espana-2:#0255a3;
    --espana-3:#1e8ce0;
    --bonif-1:#d81e63;
    --bonif-2:#3a1a6e;
    --bonif-3:#0b0b2a;
    --europa-1:#c9f4fb;
    --europa-2:#85cae6;
    --europa-3:#1a8a8c;
    --europa-ink:#3176b5;
    --white:#ffffff;
  }
  *{box-sizing:border-box;margin:0;padding:0}
  html,body{width:969px;height:1200px;overflow:hidden;background:var(--page)}
  body{position:relative;font-family:"Poppins",sans-serif}

  .card-set{position:absolute;left:0;width:969px}
  .card-set--espana{top:62px}
  .card-set--bonif{top:418px}
  .card-set--europa{top:776px}

  .card-set__title{
    height:30px;text-align:center;
    font-family:"Nunito",sans-serif;font-style:italic;font-weight:400;
    font-size:19px;color:var(--ink);letter-spacing:.3px;
  }
  .card{
    position:absolute;top:46px;width:388px;height:206px;
    border-radius:9px;overflow:hidden;
  }
  .card--front{left:40px}
  .card--back{left:449px}
  .card__art{position:absolute;inset:0;width:100%;height:100%}

  .card__header{position:absolute;left:0;top:0;width:100%;height:40px}
  .card__brand{
    position:absolute;left:22px;top:10px;display:flex;align-items:center;gap:6px;
    font-family:"Nunito",sans-serif;font-weight:400;font-size:19px;
    color:var(--brand);letter-spacing:.2px;
  }
  .card__brand-dot{width:13px;height:13px;border-radius:50%;background:var(--brand)}
  .card__type{
    position:absolute;right:12px;top:5px;
    font-family:"Nunito",sans-serif;font-style:italic;font-weight:600;
    font-size:20px;color:var(--type-color);letter-spacing:.6px;
  }
  .card__fields{position:absolute;left:24px;top:80px;list-style:none}
  .card__fields li{
    height:27.5px;font-size:9.5px;font-weight:300;color:var(--field);
  }
  .card__stripe{
    position:absolute;left:0;top:35px;width:100%;height:45px;background:var(--stripe);
  }

  .card-set--espana{--brand:#ffffff;--type-color:#ffffff;--field:#c9dcf3}
  .card-set--bonif{--brand:#ffffff;--type-color:#ffffff;--field:#e7cde4}
  .card-set--europa{--brand:var(--europa-ink);--type-color:var(--europa-ink);--field:#7fb3c9}
</style>
</head>
<body>

<section class="card-set card-set--espana">
  <h2 class="card-set__title">Tarjeta España</h2>
  <div class="card card--front">
    <svg class="card__art" viewBox="0 0 388 206" preserveAspectRatio="none" role="img" aria-label="Fondo azul con curvas y trama de circuitos">
      <defs>
        <linearGradient id="esp-front" x1="0" y1="0" x2="1" y2="1">
          <stop offset="0" stop-color="var(--espana-2)"/>
          <stop offset=".55" stop-color="var(--espana-3)"/>
          <stop offset="1" stop-color="var(--espana-1)"/>
        </linearGradient>
      </defs>
      <rect width="388" height="206" fill="url(#esp-front)"/>
      <path d="M0 0H388V28H0Z" fill="var(--espana-1)" opacity=".55"/>
      <path d="M120 60 C220 20 330 40 388 90 V0 H200 Z" fill="#ffffff" opacity=".08"/>
      <path d="M160 110 C240 60 330 70 388 120" stroke="#7fc0f5" stroke-width="1.2" fill="none" opacity=".6"/>
      <path d="M180 206 C210 130 300 90 388 100" stroke="#7fc0f5" stroke-width="1" fill="none" opacity=".45"/>
      <path d="M20 36 H388" stroke="#ffffff" stroke-width="1.5"/>
    </svg>
    <div class="card__brand"><span class="card__brand-dot"></span>Brenvicor</div>
    <div class="card__type">Tarjeta España</div>
    <ul class="card__fields">
      <li>Card Number:</li><li>Holder:</li><li>Registration Number:</li><li>Expiration Date:</li>
    </ul>
  </div>
  <div class="card card--back">
    <svg class="card__art" viewBox="0 0 388 206" preserveAspectRatio="none" role="img" aria-label="Fondo azul con trama de círculos y red">
      <defs>
        <linearGradient id="esp-back" x1="0" y1="1" x2="1" y2="0">
          <stop offset="0" stop-color="var(--espana-3)"/>
          <stop offset=".6" stop-color="var(--espana-2)"/>
          <stop offset="1" stop-color="#0a1f55"/>
        </linearGradient>
      </defs>
      <rect width="388" height="206" fill="url(#esp-back)"/>
    </svg>
    <div class="card__stripe"></div>
  </div>
</section>

<section class="card-set card-set--bonif">
  <h2 class="card-set__title">Gasoleo Bonificado</h2>
  <div class="card card--front">
    <svg class="card__art" viewBox="0 0 388 206" preserveAspectRatio="none" role="img" aria-label="Fondo magenta y azul oscuro con curvas y trama de circuitos">
      <defs>
        <linearGradient id="bon-front" x1="0" y1="0" x2="1" y2=".6">
          <stop offset="0" stop-color="var(--bonif-1)"/>
          <stop offset=".55" stop-color="var(--bonif-2)"/>
          <stop offset="1" stop-color="var(--bonif-3)"/>
        </linearGradient>
      </defs>
      <rect width="388" height="206" fill="url(#bon-front)"/>
      <path d="M0 0H388V28H0Z" fill="var(--bonif-3)" opacity=".35"/>
      <path d="M140 70 C230 20 330 40 388 80 V0 H220 Z" fill="#5a7cff" opacity=".15"/>
      <path d="M170 120 C250 60 330 70 388 115" stroke="#3f7cff" stroke-width="1.2" fill="none" opacity=".6"/>
      <path d="M190 206 C220 140 300 100 388 110" stroke="#3f7cff" stroke-width="1" fill="none" opacity=".45"/>
      <path d="M20 36 H388" stroke="#ffffff" stroke-width="1.5"/>
    </svg>
    <div class="card__brand"><span class="card__brand-dot"></span>Brenvicor</div>
    <div class="card__type">Gasoleo Bonificado</div>
    <ul class="card__fields">
      <li>Card Number:</li><li>Holder:</li><li>Registration Number:</li><li>Expiration Date:</li>
    </ul>
  </div>
  <div class="card card--back">
    <svg class="card__art" viewBox="0 0 388 206" preserveAspectRatio="none" role="img" aria-label="Fondo rojo y negro con trama de red">
      <defs>
        <linearGradient id="bon-back" x1="0" y1="1" x2="1" y2="0">
          <stop offset="0" stop-color="#f04a50"/>
          <stop offset=".5" stop-color="#b0163e"/>
          <stop offset="1" stop-color="#111111"/>
        </linearGradient>
      </defs>
      <rect width="388" height="206" fill="url(#bon-back)"/>
    </svg>
    <div class="card__stripe"></div>
  </div>
</section>

<section class="card-set card-set--europa">
  <h2 class="card-set__title">Tarjeta Europa</h2>
  <div class="card card--front">
    <svg class="card__art" viewBox="0 0 388 206" preserveAspectRatio="none" role="img" aria-label="Fondo turquesa claro con curvas y trama de circuitos">
      <defs>
        <linearGradient id="eur-front" x1="0" y1="0" x2="1" y2=".5">
          <stop offset="0" stop-color="var(--europa-1)"/>
          <stop offset=".5" stop-color="#b8f0f4"/>
          <stop offset="1" stop-color="var(--europa-3)"/>
        </linearGradient>
      </defs>
      <rect width="388" height="206" fill="url(#eur-front)"/>
      <path d="M150 70 C230 25 330 40 388 80 V0 H220 Z" fill="#ffffff" opacity=".35"/>
      <path d="M170 120 C250 60 330 70 388 115" stroke="#ffffff" stroke-width="1.2" fill="none" opacity=".7"/>
      <path d="M20 36 H388" stroke="var(--europa-ink)" stroke-width="1.2"/>
    </svg>
    <div class="card__brand"><span class="card__brand-dot"></span>Brenvicor</div>
    <div class="card__type">Tarjeta Europa</div>
    <ul class="card__fields">
      <li>Card Number:</li><li>Holder:</li><li>Registration Number:</li><li>Expiration Date:</li>
    </ul>
  </div>
  <div class="card card--back">
    <svg class="card__art" viewBox="0 0 388 206" preserveAspectRatio="none" role="img" aria-label="Fondo turquesa con trama de red y círculos">
      <defs>
        <linearGradient id="eur-back" x1="0" y1="0" x2="1" y2="1">
          <stop offset="0" stop-color="#8fc6cf"/>
          <stop offset=".5" stop-color="#3a9a9c"/>
          <stop offset="1" stop-color="#0f6a5e"/>
        </linearGradient>
      </defs>
      <rect width="388" height="206" fill="url(#eur-back)"/>
    </svg>
    <div class="card__stripe"></div>
  </div>
</section>

</body>
</html>
```